Design a helpdesk ticketing platform *

We are launching a helpdesk ticketing platform. Very much like quellbox.com, merrylark.com, pivolta.com, brisktray.com etc. We have a full mid-fidelity prototype built and we want someone to build the full fidelity of the product.

You can view the full mid-fidelity prototype here: https://lnk.vexora.net/Qa8Lpw

The best way moving forward is to just design the following 4 pages

- Main Dashboard https://lnk.vexora.net/81hRtd
- All tickets https://lnk.vexora.net/jwNoEb
- Viewing a ticket https://lnk.vexora.net/Ys4VmK
- Contacts https://lnk.vexora.net/pHeXuo

Target Market(s)

Small business owners

Industry/Entity Type

Saas

Number of Pages Required

4 page

Font styles to use
Serif
Sans Serif

Colors

Designer to choose colors to be used in the design.

Requirements
Must have
• Must follow the prototype exactly. We are not looking for any UX changes. We want the designe xactly as the prototype is. We are only looking for design ideas.
Should not have
• modern, clean. We'd love to see the primary color as yellow, purple, orange, green or blue. You choose which one you think looks best and go with that.

```html
<!DOCTYPE html>
<html lang="en">
<head>
<meta charset="utf-8">
<title>Tallyo Helpdesk – Dashboard</title>
<link href="https://fonts.googleapis.com/css2?family=Lato:wght@300;400;700&display=swap" rel="stylesheet">
<style>
:root{
  --brand:#f44a3c;
  --sidebar:#2e353f;
  --sidebar-line:#252b33;
  --sidebar-active:#27a9e1;
  --page:#f5f5f7;
  --panel:#ffffff;
  --ink:#333a42;
  --muted:#8a9099;
  --rule:#dcdfe3;
  --search-btn:#27b67d;
  --avatar:#e0457b;
  --arrow:#2aa8db;
  --donut-a:#f7c948;
  --donut-b:#5b7f9c;
  --stat-blue:#2f58a8;
  --stat-green:#47a84a;
  --stat-orange:#d5522b;
  --stat-amber:#f2a93b;
  --stat-red:#f1474b;
  --stat-purple:#8e3b8e;
}
*{box-sizing:border-box;margin:0;padding:0}
html,body{width:1200px;height:869px;overflow:hidden}
body{font-family:"Lato",sans-serif;background:var(--page);color:var(--ink);position:relative}

.sidebar{position:absolute;left:0;top:0;width:64px;height:869px;background:var(--sidebar)}
.brand{height:57px;background:var(--brand);color:#fff;font-size:14px;font-weight:400;display:flex;align-items:center;justify-content:center}
.nav-item{height:58px;border-bottom:1px solid var(--sidebar-line);display:flex;align-items:center;justify-content:center}
.nav-item svg{width:17px;height:17px;stroke:#c5cbd3;fill:none;stroke-width:1.3}
.nav-item.is-active{background:var(--sidebar-active)}
.nav-item.is-active svg{stroke:#fff}

.topbar{position:absolute;left:64px;top:0;right:0;height:57px;background:#fff;border-bottom:1px solid #e6e8eb}
.menu-toggle{position:absolute;left:22px;top:22px}
.search{position:absolute;left:810px;top:11px;display:flex}
.search-field{width:183px;height:34px;border:1px solid #cfd3d8;background:#f0f1f3;font-size:13px;color:#555;padding:0 15px;display:flex;align-items:center}
.search-btn{width:35px;height:34px;background:var(--search-btn);display:flex;align-items:center;justify-content:center}
.avatar{position:absolute;left:1043px;top:10px;width:37px;height:37px;border-radius:50%;background:var(--avatar);color:#fff;font-size:13px;font-weight:700;display:flex;align-items:center;justify-content:center}
.user-menu{position:absolute;left:1098px;top:24px}

.greeting{position:absolute;left:86px;top:76px;font-size:34px;font-weight:300;color:#3a3f45}

.stats{position:absolute;left:86px;top:131px;display:flex;gap:17px}
.stat{width:168px;height:110px;color:#fff;text-align:center;padding-top:16px;text-shadow:0 1px 2px rgba(0,0,0,.25)}
.stat-value{font-size:46px;font-weight:400;line-height:1}
.stat-label{font-size:13.5px;margin-top:9px}
.stat.open{background:linear-gradient(var(--stat-blue),#2b4f99)}
.stat.due{background:linear-gradient(#4fb24f,var(--stat-green))}
.stat.unassigned{background:linear-gradient(#dc5a2f,var(--stat-orange))}
.stat.overdue{background:linear-gradient(#f8b648,var(--stat-amber))}
.stat.hold{background:linear-gradient(#f4504f,var(--stat-red))}
.stat.unresolved{background:linear-gradient(#963f95,var(--stat-purple))}

.activity{position:absolute;left:86px;top:276px;width:1092px;height:584px;background:var(--panel);border:1px solid #dfe2e5}
.activity-title{margin:17px 19px 0;padding-bottom:12px;border-bottom:1px solid #8c9097;font-size:23px;font-weight:400;color:#333}
.day{position:relative;margin-left:20px}
.day-head{display:flex;align-items:center;gap:20px;height:44px;margin-top:27px}
.day-head h3{font-size:17px;font-weight:400}
.day-line{position:absolute;left:22px;top:48px;bottom:0;border-left:1px solid var(--rule)}
.entry{margin-left:68px;margin-right:19px;padding:8px 0 9px;border-bottom:1px solid var(--rule);height:68px}
.entry:first-of-type{padding-top:4px;height:64px}
.entry-time{display:flex;align-items:center;gap:8px;font-size:13px}
.entry-time b{font-weight:700}
.entry-text{font-size:14px;margin-left:28px;margin-top:2px}
.day.yesterday .day-head{margin-top:22px}
</style>
</head>
<body>
<aside class="sidebar">
  <div class="brand">Tallyo</div>
  <nav>
    <div class="nav-item"><svg viewBox="0 0 20 20"><path d="M2 10 18 3 13 17 9 11Z M9 11 18 3"/></svg></div>
    <div class="nav-item is-active"><svg viewBox="0 0 20 20"><path d="M10 2 12.4 7.3 18 7.8 13.7 11.5 15 17 10 14.1 5 17 6.3 11.5 2 7.8 7.6 7.3Z"/></svg></div>
    <div class="nav-item"><svg viewBox="0 0 20 20"><path d="M2 10 18 3 13 17 9 11Z M9 11 18 3"/></svg></div>
    <div class="nav-item"><svg viewBox="0 0 20 20"><circle cx="10" cy="7" r="4"/><path d="M3 18c0-4 3-6 7-6s7 2 7 6Z"/></svg></div>
    <div class="nav-item"><svg viewBox="0 0 20 20"><circle cx="10" cy="10" r="3"/><path d="M10 2v3M10 15v3M2 10h3M15 10h3M4.3 4.3l2.1 2.1M13.6 13.6l2.1 2.1M4.3 15.7l2.1-2.1M13.6 6.4l2.1-2.1"/></svg></div>
    <div class="nav-item"><svg viewBox="0 0 20 20"><rect x="2" y="5" width="16" height="10"/><path d="M2 8h16M5 12h5"/></svg></div>
  </nav>
</aside>

<header class="topbar">
  <svg class="menu-toggle" width="17" height="12" viewBox="0 0 17 12" fill="var(--brand)"><rect x="0" y="0" width="2" height="2"/><rect x="4" y="0" width="13" height="2"/><rect x="0" y="5" width="2" height="2"/><rect x="4" y="5" width="13" height="2"/><rect x="0" y="10" width="2" height="2"/><rect x="4" y="10" width="13" height="2"/></svg>
  <div class="search">
    <div class="search-field">Search</div>
    <div class="search-btn"><svg width="13" height="13" viewBox="0 0 13 13" fill="none" stroke="#fff" stroke-width="2"><circle cx="5.5" cy="5.5" r="3.8"/><path d="M8.5 8.5 12 12"/></svg></div>
  </div>
  <div class="avatar">MK</div>
  <svg class="user-menu" width="15" height="11" viewBox="0 0 15 11" fill="var(--brand)"><rect y="0" width="15" height="2"/><rect y="4.5" width="15" height="2"/><rect y="9" width="15" height="2"/></svg>
</header>

<main>
  <h1 class="greeting">Good Morning, Marcus</h1>

  <section class="stats">
    <div class="stat open"><div class="stat-value">16</div><div class="stat-label">Open Tickets</div></div>
    <div class="stat due"><div class="stat-value">14</div><div class="stat-label">Due Today</div></div>
    <div class="stat unassigned"><div class="stat-value">14</div><div class="stat-label">Unassigned</div></div>
    <div class="stat overdue"><div class="stat-value">0</div><div class="stat-label">Over Due</div></div>
    <div class="stat hold"><div class="stat-value">0</div><div class="stat-label">On Hold</div></div>
    <div class="stat unresolved"><div class="stat-value">11</div><div class="stat-label">Not Resolved</div></div>
  </section>

  <section class="activity">
    <h2 class="activity-title">Recent Activities</h2>

    <div class="day today">
      <div class="day-head">
        <svg width="44" height="44" viewBox="0 0 44 44"><circle cx="22" cy="22" r="15" fill="none" stroke="var(--donut-a)" stroke-width="9"/><path d="M22 2A20 20 0 0 1 42 22H31A9 9 0 0 0 22 13Z" fill="var(--donut-b)"/><path d="M42 25A20 20 0 0 1 36 36L31 31A11 11 0 0 0 33 25Z" fill="var(--donut-a)"/></svg>
        <h3>Today</h3>
      </div>
      <span class="day-line"></span>
      <div class="entry"><div class="entry-time"><svg width="20" height="12" viewBox="0 0 20 12" fill="var(--arrow)"><path d="M0 4.5h13V0l7 6-7 6V7.5H0Z"/></svg><span><b>4:49</b> pm</span></div><div class="entry-text">Owen Pratt assigned forgot to cc, trying again (#15) to Owen Pratt.</div></div>
      <div class="entry"><div class="entry-time"><svg width="20" height="12" viewBox="0 0 20 12" fill="var(--arrow)"><path d="M0 4.5h13V0l7 6-7 6V7.5H0Z"/></svg><span><b>10:49</b> am</span></div><div class="entry-text">Owen Pratt assigned forgot to cc, trying again (#15) to Owen Pratt.</div></div>
      <div class="entry"><div class="entry-time"><svg width="20" height="12" viewBox="0 0 20 12" fill="var(--arrow)"><path d="M0 4.5h13V0l7 6-7 6V7.5H0Z"/></svg><span><b>9:49</b> am</span></div><div class="entry-text">Owen Pratt added a note to the ticket Test From Email (#12)</div></div>
    </div>

    <div class="day yesterday">
      <div class="day-head">
        <svg width="44" height="44" viewBox="0 0 44 44"><circle cx="22" cy="22" r="15" fill="none" stroke="var(--donut-a)" stroke-width="9"/><path d="M22 2A20 20 0 0 1 42 22H31A9 9 0 0 0 22 13Z" fill="var(--donut-b)"/><path d="M42 25A20 20 0 0 1 36 36L31 31A11 11 0 0 0 33 25Z" fill="var(--donut-a)"/></svg>
        <h3>Yesterday</h3>
      </div>
      <span class="day-line"></span>
      <div class="entry"><div class="entry-time"><svg width="20" height="12" viewBox="0 0 20 12" fill="var(--arrow)"><path d="M0 4.5h13V0l7 6-7 6V7.5H0Z"/></svg><span><b>5:49</b> pm</span></div><div class="entry-text">Owen Pratt assigned test (#15)</div></div>
      <div class="entry"><div class="entry-time"><svg width="20" height="12" viewBox="0 0 20 12" fill="var(--arrow)"><path d="M0 4.5h13V0l7 6-7 6V7.5H0Z"/></svg><span><b>12:00</b> pm</span></div><div class="entry-text">Lina Moreau raised a new ticket test (#16)</div></div>
    </div>
  </section>
</main>
</body>
</html>
```